***PLASTIC*** Business Card Design

1 sided business card design
The card will be screen printed on plastic, so colour and fonts must be strong.

Must use the colours in the logo eps attached (Black/Ivory/White). Other colour(s) can be added.

Four (4) examples of how the logo can be printed are included in the logo eps attached.

The business card should highlight the logo. The card will be given to architects, interior designers and builders. It should look sophisticated but also innovative.

Do not cover the whole card with colour as it is important than some of the frosted plastic card is visible.

Be creative.

Target Market(s)

architects, interior designers and builders and wealthy home owners

Industry/Entity Type

Plastic

Requirements
Must have
• Must use the colours in the logo eps attached (Black/Ivory/White). Other colour(s) can be added if necessary.

The font is Square721 ExBT but has been a little thickened. It is not essential that you use this font. The name should be a stronger version of the font than other details.

The card will be printed on PVC - see http://www.voltrap.com.au/pricelistbcardsplastic.php

Final artwork must be print ready. You must use the printing spec at http://www.voltrap.com.au/2011%20PVC-TW.pdf

The actual details to be typeset ono the card are:

Dorian Welch

Mobile: 0412 806133
email: info@halcoworks.com.au
www.halcoworks.com.au

PO Box 53, Altona, Vic 3018

Plastering | Rendering | Cornicing

```html
<!DOCTYPE html>
<html lang="en">
<head>
<meta charset="utf-8">
<title>Halco Plastering – Business Card</title>
<link rel="stylesheet" href="https://fonts.googleapis.com/css2?family=Tinos:wght@400;700&display=swap">
<style>
  :root {
    --backdrop: #d7dcdb;
    --frost: #eef1f1;
    --frost-edge: #c9cfcf;
    --band-black: #050505;
    --ivory: #efe3c2;
    --white: #ffffff;
    --ink: #1a1a1a;
  }
  * { margin: 0; padding: 0; box-sizing: border-box; }
  html, body {
    width: 1200px;
    height: 848px;
    overflow: hidden;
    background: var(--backdrop);
  }
  .card {
    position: absolute;
    left: 150px;
    top: 164px;
    width: 900px;
    height: 520px;
    border-radius: 26px;
    background: var(--frost);
    border: 1px solid var(--frost-edge);
    overflow: hidden;
    font-family: "Tinos", "Times New Roman", serif;
  }
  .band {
    position: absolute;
    left: 0;
    top: 130px;
    width: 100%;
    height: 240px;
    background: var(--band-black);
  }
  .brand {
    position: absolute;
    left: 64px;
    top: 96px;
    display: flex;
    align-items: center;
    gap: 16px;
    color: var(--ivory);
    font-weight: 700;
    font-size: 40px;
    letter-spacing: 2px;
    text-transform: uppercase;
  }
  .brand-mark {
    width: 26px;
    height: 26px;
    background: var(--ivory);
  }
  .holder-name {
    position: absolute;
    right: 56px;
    top: 28px;
    color: var(--white);
    font-size: 22px;
    font-weight: 700;
  }
  .contact {
    position: absolute;
    right: 56px;
    bottom: 30px;
    text-align: right;
    color: var(--white);
    font-size: 19px;
    line-height: 1.35;
  }
  .footer {
    position: absolute;
    left: 64px;
    right: 56px;
    top: 392px;
    color: var(--ink);
    font-size: 19px;
    line-height: 1.35;
  }
  .postal {
    padding-left: 150px;
  }
  .services {
    margin-top: 30px;
    display: flex;
    justify-content: space-between;
    align-items: baseline;
  }
  .separator { color: var(--ink); }
</style>
</head>
<body>
  <section class="card" aria-label="Halco Plastering business card">
    <div class="band">
      <div class="brand"><span class="brand-mark"></span>Halco Plastering</div>
      <div class="holder-name">Dorian Welch</div>
      <div class="contact">
        <p>Mobile: 0412 806133</p>
        <p>email: info@halcoworks.com.au</p>
        <p>www.halcoworks.com.au</p>
      </div>
    </div>
    <div class="footer">
      <p class="postal">PO Box 53, Altona, Vic 3018</p>
      <p class="services">
        <span class="service">Plastering</span>
        <span class="separator">|</span>
        <span class="service">Rendering</span>
        <span class="separator">|</span>
        <span class="service">Cornicing</span>
      </p>
    </div>
  </section>
</body>
</html>
```